Business Card Design

We need a business card design for a consulting firm which provides safety and risk management consulting services for public venues, hotels and tourist attractions. The business card design should include the attached logo unedited with a design based on incorporating the existing logo with a design of geometric patterns or lines on a predominantly white background.

Industry/Entity Type

Business

Contact Information for Business Card

Dane Morravik
Director & Principal Consultant

Ph: +61 (0) 478506 214
PO Box 456 Brenmoor Vale, NSW Australia 2611
info@corvalrisksafety.example

(back of card to include website www.corvalrisksafety.example

```html
<!DOCTYPE html>
<html lang="en">
<head>
<meta charset="utf-8">
<title>Corval Risk &amp; Safety – Business Card</title>
<link rel="stylesheet" href="https://fonts.googleapis.com/css2?family=Ubuntu:wght@500;700&family=Open+Sans:wght@400;600&display=swap">
<style>
  :root {
    --brand-blue: #3aa3dc;
    --brand-green: #7dbb42;
    --ink: #3a3a3a;
    --card-white: #ffffff;
    --backdrop: #e9ebee;
  }
  * { box-sizing: border-box; margin: 0; padding: 0; }
  html, body { width: 1200px; height: 900px; overflow: hidden; }
  body {
    background: var(--backdrop);
    display: flex;
    flex-direction: column;
    align-items: center;
    justify-content: center;
    gap: 50px;
    font-family: "Open Sans", sans-serif;
    color: var(--ink);
  }
  .card {
    position: relative;
    width: 630px;
    height: 360px;
    overflow: hidden;
    box-shadow: 0 6px 18px rgba(0,0,0,0.12);
  }
  .card-front { background: var(--card-white); }
  .card-back { background: var(--brand-blue); display: flex; align-items: center; justify-content: center; }

  .corner-accent {
    position: absolute;
    top: -90px;
    right: -90px;
    width: 260px;
    height: 260px;
    border: 22px solid var(--brand-blue);
    border-radius: 50%;
  }

  .brand {
    position: absolute;
    left: 48px;
    top: 92px;
    display: flex;
    align-items: center;
    gap: 12px;
  }
  .brand-mark {
    width: 30px;
    height: 30px;
    border-radius: 50%;
    background: var(--brand-green);
  }
  .brand-name {
    font-family: "Ubuntu", sans-serif;
    font-weight: 700;
    font-size: 30px;
    color: var(--brand-blue);
    letter-spacing: 0.5px;
  }

  .person { position: absolute; left: 48px; top: 168px; }
  .person-name {
    font-family: "Ubuntu", sans-serif;
    font-weight: 700;
    font-size: 24px;
    color: var(--brand-blue);
  }
  .person-title {
    font-family: "Ubuntu", sans-serif;
    font-weight: 500;
    font-size: 15px;
    color: var(--brand-green);
    margin-top: 2px;
  }
  .pulse-rule { display: block; margin-top: 6px; }

  .contact-list { position: absolute; left: 48px; top: 262px; list-style: none; }
  .contact-item {
    display: flex;
    align-items: center;
    gap: 10px;
    font-size: 13.5px;
    line-height: 24px;
  }
  .contact-icon { width: 14px; height: 14px; flex: none; }

  .back-brand { display: flex; align-items: center; gap: 16px; }
  .back-mark {
    width: 40px; height: 40px;
    border: 3px solid var(--card-white);
    border-radius: 50%;
  }
  .website {
    font-family: "Open Sans", sans-serif;
    font-size: 20px;
    color: var(--card-white);
    letter-spacing: 0.3px;
  }
</style>
</head>
<body>
  <section class="card card-front" aria-label="Card front">
    <div class="corner-accent"></div>

    <div class="brand">
      <span class="brand-mark"></span>
      <span class="brand-name">Corval Risk &amp; Safety</span>
    </div>

    <div class="person">
      <p class="person-name">Dane Morravik</p>
      <p class="person-title">Director &amp; Principal Consultant</p>
      <svg class="pulse-rule" width="250" height="14" viewBox="0 0 250 14">
        <polyline points="0,8 20,8 25,2 30,13 35,8 250,8" fill="none" stroke="#3aa3dc" stroke-width="1.5"/>
      </svg>
    </div>

    <ul class="contact-list">
      <li class="contact-item">
        <svg class="contact-icon" viewBox="0 0 14 14"><rect x="3.5" y="1" width="7" height="12" rx="1.5" fill="none" stroke="#3aa3dc" stroke-width="1.5"/></svg>
        +61 (0) 478506 214
      </li>
      <li class="contact-item">
        <svg class="contact-icon" viewBox="0 0 14 14"><path d="M7 13 C3 8 2.5 6.5 2.5 5 A4.5 4.5 0 0 1 11.5 5 C11.5 6.5 11 8 7 13Z" fill="#3aa3dc"/><circle cx="7" cy="5" r="1.7" fill="#fff"/></svg>
        PO Box 456 Brenmoor Vale, NSW Australia 2611
      </li>
      <li class="contact-item">
        <svg class="contact-icon" viewBox="0 0 14 14"><rect x="1" y="3" width="12" height="9" fill="#3aa3dc"/><polyline points="1,3 7,8 13,3" fill="none" stroke="#fff" stroke-width="1.2"/></svg>
        info@corvalrisksafety.example
      </li>
    </ul>
  </section>

  <section class="card card-back" aria-label="Card back">
    <div class="back-brand">
      <span class="back-mark"></span>
      <span class="website">www.corvalrisksafety.example</span>
    </div>
  </section>
</body>
</html>
```